New business card/stationary for a consulting company

I am looking for a clean and very professional looking business card for my consulting company as well as corresponding stationary. I am uploading our logo. I like simple and powerful for the feel. No graphics but I am open on everything else. Below is my contact information but would like the final to be in a version I can add my employees information into and print. Thank you.

Daniel Whitcombe
dan@fernlowadvisory.com
2837 North 9th Avenue, Summit Floor, Elm Grove, Indiana 60483
www.fernlowadvisory.com

Industry/Entity Type

Consulting

Contact Information for Business Card

Daniel Whitcombe
dan@fernlowadvisory.com
www.fernlowadvisory.com

Font styles to use
Serif
Sans Serif

Requirements
Must have
• Our logo and the business card details.
Nice to have
• our website www.fernlowadvisory.com

```html
<!DOCTYPE html>
<html lang="en">
<head>
<meta charset="utf-8">
<title>Fernlow Advisory — Business Card</title>
<link rel="stylesheet" href="https://fonts.googleapis.com/css2?family=Tenor+Sans&family=Open+Sans:wght@400;600&display=swap">
<style>
  :root {
    --navy: #13256e;
    --navy-deep: #0d1a55;
    --dusk-blue: #4a5f9c;
    --dusk-rose: #c9a0a8;
    --dusk-gold: #e3b79a;
    --white: #ffffff;
    --panel: rgba(255, 255, 255, 0.86);
    --ink: #2d3340;
    --ink-soft: #3f4655;
    --accent: #2f8fe6;
    --backdrop: #e6e6e8;
  }
  * { margin: 0; padding: 0; box-sizing: border-box; }
  html, body { width: 1200px; height: 1000px; overflow: hidden; }
  body { background: var(--backdrop); position: relative; font-family: "Open Sans", sans-serif; }

  .card { position: absolute; width: 650px; height: 390px; overflow: hidden; }
  .card--front { left: 283px; top: 43px; }
  .card--back { left: 274px; top: 517px; }

  .card__photo {
    position: absolute; inset: 0;
    background:
      radial-gradient(ellipse 45% 30% at 50% 52%, rgba(227,183,154,0.55), transparent 70%),
      linear-gradient(180deg, var(--navy-deep) 0%, var(--dusk-blue) 38%, var(--dusk-rose) 55%, var(--dusk-blue) 68%, var(--navy) 100%);
  }

  /* Front */
  .frame { position: absolute; border: 4px solid var(--white); }
  .frame--upper { left: 62px; top: 40px; width: 548px; height: 285px; }
  .frame--lower { left: 37px; top: 64px; width: 548px; height: 288px; }

  .brand-dot {
    position: absolute; left: 285px; top: 105px; width: 80px; height: 80px;
    border-radius: 50%; background: var(--accent);
  }
  .brand-name {
    position: absolute; left: 0; right: 0; top: 246px; text-align: center;
    font-family: "Tenor Sans", sans-serif; font-size: 30px; color: var(--white);
    letter-spacing: 1px;
  }
  .brand-url {
    position: absolute; left: 0; right: 0; top: 301px; text-align: center;
    font-size: 10px; color: var(--white); letter-spacing: 0.3px;
  }

  /* Back */
  .panel { position: absolute; left: 36px; top: 36px; width: 576px; height: 316px; background: var(--panel); }
  .panel__divider { position: absolute; left: 288px; top: 34px; width: 2px; height: 248px; background: var(--navy); }

  .identity { position: absolute; left: 0; width: 288px; top: 0; text-align: center; }
  .identity__mark {
    position: absolute; left: 110px; top: 70px; width: 64px; height: 64px;
    border-radius: 50%; background: var(--accent);
  }
  .identity__company {
    position: absolute; left: 0; right: 0; top: 148px;
    font-family: "Tenor Sans", sans-serif; font-size: 17px; color: var(--navy); letter-spacing: 1px;
  }
  .identity__name {
    position: absolute; left: 0; right: 0; top: 183px;
    font-family: "Tenor Sans", sans-serif; font-size: 21px; color: var(--navy); letter-spacing: 0.5px;
    text-transform: uppercase; white-space: nowrap;
  }
  .identity__name b { font-family: "Open Sans", sans-serif; font-weight: 600; }
  .identity__title {
    position: absolute; left: 0; right: 0; top: 217px;
    font-family: "Tenor Sans", sans-serif; font-size: 16px; line-height: 21px;
    color: var(--ink); letter-spacing: 4px; text-transform: uppercase;
  }

  .contact { position: absolute; left: 300px; top: 114px; width: 270px; }
  .contact__row { display: flex; align-items: baseline; margin-bottom: 11px; }
  .contact__label { width: 80px; text-align: right; font-size: 14px; color: var(--ink-soft); padding-right: 4px; flex-shrink: 0; }
  .contact__value { font-size: 11px; color: var(--ink); text-transform: uppercase; line-height: 14px; }
  .contact__value--phone { font-size: 14px; }
  .contact__value--address { text-transform: none; }
</style>
</head>
<body>

  <section class="card card--front">
    <div class="card__photo" role="img" aria-label="Photograph of business people silhouetted against tall office windows at dusk"></div>
    <div class="frame frame--upper"></div>
    <div class="frame frame--lower"></div>
    <div class="brand-dot"></div>
    <p class="brand-name">FERNLOW ADVISORY</p>
    <p class="brand-url">WWW.FERNLOWADVISORY.COM</p>
  </section>

  <section class="card card--back">
    <div class="card__photo" role="img" aria-label="Photograph of business people standing by office windows at sunset"></div>
    <div class="panel">
      <div class="identity">
        <div class="identity__mark"></div>
        <p class="identity__company">FERNLOW ADVISORY</p>
        <p class="identity__name"><b>Daniel</b> Whitcombe</p>
        <p class="identity__title">Managing<br>Director</p>
      </div>
      <div class="panel__divider"></div>
      <div class="contact">
        <div class="contact__row"><span class="contact__label">Phone:</span><span class="contact__value contact__value--phone">555 014 2290</span></div>
        <div class="contact__row"><span class="contact__label">Email:</span><span class="contact__value">dan@fernlowadvisory.com</span></div>
        <div class="contact__row"><span class="contact__label">Website:</span><span class="contact__value">www.fernlowadvisory.com</span></div>
        <div class="contact__row"><span class="contact__label">Address:</span><span class="contact__value contact__value--address">2837 North 9th Avenue,<br>Summit Floor, Elm Grove,<br>Indiana 60483</span></div>
      </div>
    </div>
  </section>

</body>
</html>
```